Newsletter Template to be emailed to clients

I require a newsletter template that I can edit and frequently update and embed into an email and send to my clients. HTML & CSS

I am seeking it to be attention grabbing, engaging and make use of social media buttons for users to further engage with Bright Pathfinders. Our business provides free career services to young professionals. Visit http://brightpathfinders-demo.net/home/

Important for the content to be able to be interactive, so clients can click onto hyperlinks and be taken to our site. The font style and colours need to match our corporate colours. The Images need to be high resolution and clear. Please submit your designs using material from our site so we can see what it could potentially look like.

Please see a template in the attachment to replicate with Bright Pathfinders colours and images. Combine image 1 and 2 together to see the whole template.
Updates

Project Deadline Extended Reason: I am not that impressed with the designs submitted. I would like more options. Added Monday, June 15, 2015

Hi All, Please note I have extended the deadline on this project because I am wanting more designs. Looking for something creative and catchy. Less font…only the most important things like heading, content etc Would like to see a section for career tools. Many thanks, Wendy

Target Market(s)

20-30 year olds

Industry/Entity Type

Seeking

Font styles to use
Sans Serif

Requirements
Must have
• Bright Pathfinders logo - attached.
• Corporate Colours with font.
• Highlighted Career Tools separate from Blogs.
• Grey R66 G73 B74
• White R242 G240 B230
• Teal R38 G128 B138
• Clean white backdrop.
Nice to have
• Something modern and professional but trendy so it catches the attention of 20-30 year olds.

```html
<!DOCTYPE html>
<html lang="en">
<head>
<meta charset="utf-8">
<title>Bright Pathfinders Newsletter</title>
<link rel="stylesheet" href="https://fonts.googleapis.com/css2?family=Open+Sans:ital,wght@0,400;0,600;0,700;1,400;1,600&family=Vollkorn:wght@400&display=swap">
<style>
  :root {
    --teal: #26808a;
    --grey: #42494a;
    --text: #3d3d3d;
    --divider: #999999;
    --paper: #ffffff;
    --photo-light: #e9ebeb;
    --photo-mid: #d6d9da;
  }
  * { box-sizing: border-box; margin: 0; padding: 0; }
  html, body { width: 875px; height: 1200px; overflow: hidden; background: var(--paper); }
  body { font-family: "Open Sans", Arial, sans-serif; color: var(--text); }
  a { color: inherit; text-decoration: none; }

  .newsletter { width: 656px; margin: 0 auto; }

  .masthead { height: 116px; display: flex; justify-content: space-between; align-items: center; padding-bottom: 6px; }
  .brand-name { font-family: "Open Sans", Arial, sans-serif; font-weight: 700; color: var(--teal); font-size: 28px; line-height: 34px; }
  .social-header { display: flex; gap: 20px; }
  .social-header a { width: 46px; height: 46px; border: 2.5px solid var(--teal); border-radius: 50%; display: block; }

  .hero { width: 656px; height: 328px; background: linear-gradient(160deg, var(--photo-light), var(--photo-mid)); }

  .headline { margin-top: 26px; text-align: center; color: var(--teal); font-weight: 700; font-size: 37px; line-height: 46px; text-transform: uppercase; letter-spacing: 0.2px; }

  .intro { margin-top: 14px; font-family: "Vollkorn", Georgia, serif; font-size: 17.5px; line-height: 23.5px; color: var(--text); }
  .intro p + p { margin-top: 23px; }

  .share { margin-top: 14px; display: flex; justify-content: space-between; align-items: center; }
  .share-label { color: var(--teal); font-style: italic; font-weight: 600; font-size: 18px; }
  .share-links { display: flex; gap: 22px; }
  .share-links a { width: 26px; height: 26px; background: var(--teal); border-radius: 50%; display: block; }

  .cta { margin-top: 20px; text-align: center; }
  .button { display: block; width: 219px; height: 46px; margin: 0 auto; font-weight: 600; font-size: 23px; line-height: 44px; text-transform: uppercase; }
  .button-primary { background: var(--teal); color: #fff; }
  .button-outline { border: 1.5px solid var(--teal); color: var(--teal); height: 44px; line-height: 41px; font-size: 22px; }
  .cta-note { font-style: italic; font-size: 17px; color: var(--text); text-transform: uppercase; line-height: 24px; }
  .cta-with { margin: 10px 0 9px; }
  .cta-more { margin-top: 10px; }

  .sections { margin-top: 28px; border-top: 1px solid var(--teal); border-bottom: 1px solid var(--teal); height: 48px; display: flex; align-items: center; justify-content: space-between; }
  .sections a { color: var(--teal); font-weight: 600; font-size: 23px; text-transform: uppercase; padding: 0 12px; border-left: 1px solid var(--teal); line-height: 26px; }
  .sections a:first-child { border-left: none; padding-left: 0; }
  .sections a:last-child { padding-right: 0; }

  .footer { text-align: center; color: var(--grey); font-weight: 600; font-size: 19px; }
  .footer-links { margin-top: 30px; }
  .footer-links span { color: var(--divider); font-weight: 400; margin: 0 6px; }
  .copyright { margin-top: 18px; }
</style>
</head>
<body>
<div class="newsletter">
  <header class="masthead">
    <a class="brand" href="http://brightpathfinders-demo.net/home/">
      <span class="brand-name">Bright Pathfinders</span>
    </a>
    <nav class="social-header" aria-label="Follow us">
      <a href="#" aria-label="Social network 1"></a>
      <a href="#" aria-label="Social network 2"></a>
      <a href="#" aria-label="Social network 3"></a>
      <a href="#" aria-label="Social network 4"></a>
    </nav>
  </header>

  <div class="hero" role="img" aria-label="Overhead photo of hands typing on a laptop on a white desk with a glass, remote and pen pot"></div>

  <h1 class="headline">The resume mistakes you’ll<br>want to fix ASAP</h1>

  <div class="intro">
    <p>Let’s say it takes you five minutes to read this article. In the same time span, a hiring manager will look at around 50 resumes.</p>
    <p>That certainly doesn’t seem like enough time to absorb all your accomplishments, skills, experiences, and qualifications. And it’s not! So it’s critical that there aren’t any errors on your resume—because for every mistake, another precious second is taken away from looking at what really matters.</p>
  </div>

  <div class="share">
    <span class="share-label">SHARE THIS ARTICLE</span>
    <nav class="share-links" aria-label="Share">
      <a href="#" aria-label="Share 1"></a>
      <a href="#" aria-label="Share 2"></a>
      <a href="#" aria-label="Share 3"></a>
      <a href="#" aria-label="Share 4"></a>
    </nav>
  </div>

  <div class="cta">
    <a class="button button-primary" href="http://brightpathfinders-demo.net/home/">Find out</a>
    <p class="cta-note cta-with">with</p>
    <a class="button button-outline" href="http://brightpathfinders-demo.net/home/">Career tools</a>
    <p class="cta-note cta-more">Check out more<br>personalized updates!</p>
  </div>

  <nav class="sections">
    <a href="#">Newsroom</a>
    <a href="#">Money</a>
    <a href="#">Life at work</a>
    <a href="#">The BP Journey</a>
  </nav>

  <footer class="footer">
    <p class="footer-links"><a href="#">View in browser</a><span>|</span><a href="#">Terms</a><span>|</span><a href="#">Unsubscribe</a></p>
    <p class="copyright">© 2015 Company</p>
  </footer>
</div>
</body>
</html>
```